Business card required for IT Consultancy Business - Bluefern Consulting.
Company provides the whole nine yards of services across IT Architecture, design and execution.
Basically we provide consulting services to help businesses make sure their technology is enabling their business strategy.
Design for front and back required.
We would like the front of the card to inlcude:
Name
Title
Mobile number
email address
www.BFQ.com.au
Company logos attached.
Thank you
Industry/Entity Type
Business
Contact Information for Business Card
Name
Title
Mobile number
email address
www.BFQ.com.au
Look and feel
Each slider illustrates characteristics of the customer's brand and the style your logo design should communicate.

```html
<!DOCTYPE html>
<html lang="en">
<head>
<meta charset="utf-8">
<title>Bluefern Consulting – Business Card</title>
<link href="https://fonts.googleapis.com/css2?family=Lato:wght@400;700;900&display=swap" rel="stylesheet">
<style>
  :root {
    --orange: #f05a28;
    --blue: #1177c0;
    --white: #ffffff;
    --paper: #f6f6f6;
    --ink: #1e1e1e;
    --stage: #ececec;
    --divider: #e8474a;
  }
  * { box-sizing: border-box; margin: 0; padding: 0; }
  html, body {
    width: 1200px; height: 586px; overflow: hidden;
    background: var(--stage);
    font-family: "Lato", sans-serif;
  }
  .canvas { position: relative; width: 1200px; height: 586px; }
  .card {
    position: absolute; top: 129px;
    width: 500px; height: 300px; overflow: hidden;
  }

  /* Card face with brand */
  .card--brand { left: 62px; background: var(--orange); color: var(--white); }
  .brand-mark {
    position: absolute; left: 24px; top: 186px;
    display: flex; align-items: center; gap: 10px;
    font-weight: 900; font-size: 30px; line-height: 1; letter-spacing: 0.5px;
  }
  .brand-dot { width: 26px; height: 26px; border-radius: 50%; background: var(--white); flex: none; }
  .brand-web {
    position: absolute; left: 26px; top: 259px;
    font-weight: 700; font-style: italic; font-size: 12px; letter-spacing: 5.2px;
  }

  /* Card face with contact details */
  .card--contact { left: 619px; background: var(--paper); color: var(--ink); }
  .contact-mark {
    position: absolute; left: 52px; top: 118px;
    display: flex; align-items: center; gap: 10px;
    color: var(--blue); font-weight: 900; font-size: 22px; line-height: 1.05;
  }
  .contact-mark .brand-dot { background: var(--orange); width: 22px; height: 22px; }
  .divider {
    position: absolute; left: 240px; top: 75px; width: 2px; height: 144px;
    background: linear-gradient(to bottom, transparent, var(--divider) 40%, var(--divider) 60%, transparent);
  }
  .person { position: absolute; left: 268px; top: 85px; }
  .person-name { color: var(--orange); font-weight: 700; font-size: 14.5px; }
  .person-title { font-size: 12px; margin-top: 3px; }
  .contact-list { position: absolute; left: 268px; top: 141px; list-style: none; }
  .contact-item {
    display: flex; align-items: center; gap: 7px;
    height: 24px; font-size: 12px;
  }
  .contact-icon { width: 17px; height: 17px; flex: none; }
  .band-orange {
    position: absolute; left: 0; bottom: 0; width: 300px; height: 15px;
    background: var(--orange);
    clip-path: polygon(0 0, 100% 0, calc(100% - 15px) 100%, 0 100%);
  }
  .band-blue {
    position: absolute; right: 0; bottom: 0; width: 218px; height: 26px;
    background: var(--blue); color: var(--white);
    clip-path: polygon(22px 0, 100% 0, 100% 100%, 0 100%);
    font-weight: 700; font-size: 11px; letter-spacing: 3.4px;
    display: flex; align-items: center; justify-content: flex-end; padding-right: 34px;
  }
</style>
</head>
<body>
<main class="canvas">
  <section class="card card--brand" aria-label="Card front">
    <div class="brand-mark"><span class="brand-dot"></span><span>Bluefern<br>Consulting</span></div>
    <div class="brand-web">www.BFQ.com.au</div>
  </section>

  <section class="card card--contact" aria-label="Card back">
    <div class="contact-mark"><span class="brand-dot"></span><span>Bluefern<br>Consulting</span></div>
    <div class="divider"></div>
    <div class="person">
      <div class="person-name">Claire Dumont-Varenne</div>
      <div class="person-title">Sales Director</div>
    </div>
    <ul class="contact-list">
      <li class="contact-item">
        <svg class="contact-icon" viewBox="0 0 20 20" aria-hidden="true">
          <circle cx="10" cy="10" r="10" fill="var(--blue)"/>
          <path d="M6 8.5c0-1.6 1.8-2.5 4-2.5s4 .9 4 2.5v.8h-2.2V8.2H8.2v1.1H6z M7 11l1.5-1.5h3L13 11v3H7z" fill="#fff"/>
        </svg>
        <span>+33 6 41 28 90 17</span>
      </li>
      <li class="contact-item">
        <svg class="contact-icon" viewBox="0 0 20 20" aria-hidden="true">
          <circle cx="10" cy="10" r="10" fill="var(--blue)"/>
          <rect x="7" y="5" width="6" height="3" fill="#fff"/>
          <rect x="5" y="8.5" width="10" height="4.5" rx="1" fill="#fff"/>
          <rect x="7" y="12" width="6" height="3" fill="#fff" stroke="var(--blue)" stroke-width=".8"/>
        </svg>
        <span>+33 9 58 34 20 66</span>
      </li>
      <li class="contact-item">
        <svg class="contact-icon" viewBox="0 0 20 20" aria-hidden="true">
          <circle cx="10" cy="10" r="10" fill="var(--blue)"/>
          <rect x="5" y="6.5" width="10" height="7" fill="#fff"/>
          <path d="M5 6.5l5 4 5-4" fill="none" stroke="var(--blue)" stroke-width="1"/>
        </svg>
        <span>claire@maisonverdier.fr</span>
      </li>
    </ul>
    <div class="band-orange"></div>
    <div class="band-blue">www.BFQ.com.au</div>
  </section>
</main>
</body>
</html>
```